Business Consultancy Business Card Design

Business Card design required for Business Analysis and Project Consultancy business based in Scotland.

Company Name - Brackwell Consulting

Back - Company Logo

Front Details

Euan Brackwell
07402 916 254
euan.brackwell@brackwellconsulting.example
http://www.brackwellconsulting.example

Colours should match the logo colours but I am open to design ideas.

```html
<!DOCTYPE html>
<html lang="en">
<head>
<meta charset="utf-8">
<title>Brackwell Consulting – Business Card</title>
<link href="https://fonts.googleapis.com/css2?family=Roboto:wght@300;400&display=swap" rel="stylesheet">
<style>
  :root {
    --brand-blue: #1f9bd7;
    --brand-green: #5bad35;
    --card-white: #ffffff;
    --ink: #5a5a5a;
    --ink-soft: #6e6e6e;
    --backdrop: #ececec;
  }
  * { box-sizing: border-box; margin: 0; padding: 0; }
  html, body {
    width: 1200px; height: 873px; overflow: hidden;
    background: var(--backdrop);
    font-family: "Roboto", Arial, sans-serif;
  }
  .sheet {
    width: 1200px; height: 873px;
    display: flex; align-items: center; justify-content: center; gap: 60px;
  }
  .card {
    position: relative;
    width: 520px; height: 298px;
    background: var(--card-white);
    overflow: hidden;
    box-shadow: 0 2px 10px rgba(0,0,0,0.12);
  }
  .card__bands { position: absolute; inset: 0; width: 100%; height: 100%; }
  .band-blue { fill: var(--brand-blue); }
  .band-green { fill: var(--brand-green); }

  /* front */
  .front__brand {
    position: absolute; left: 34px; top: 58px;
    display: flex; align-items: center; gap: 12px;
  }
  .brand__dot {
    width: 46px; height: 46px; border-radius: 50%;
    background: var(--brand-blue);
  }
  .brand__name {
    font-weight: 400; font-size: 17px; letter-spacing: 1px;
    text-transform: uppercase; color: var(--ink);
  }
  .front__details {
    position: absolute; left: 170px; top: 122px;
    color: var(--ink);
  }
  .person__name { font-weight: 300; font-size: 30px; line-height: 1; }
  .person__role { font-weight: 300; font-size: 14px; margin: 4px 0 12px 2px; color: var(--ink-soft); }
  .contact { list-style: none; }
  .contact__item {
    display: flex; align-items: center; gap: 8px;
    font-size: 12.5px; line-height: 19px; color: var(--ink);
  }
  .contact__icon { width: 12px; height: 12px; flex: none; }

  /* back */
  .back__stripe {
    position: absolute; left: 0; right: 0; top: 112px; height: 74px;
    background: var(--card-white);
    display: flex; align-items: center; justify-content: center; gap: 16px;
  }
  .back__stripe .brand__dot { width: 40px; height: 40px; }
  .back__divider { width: 1px; height: 40px; background: var(--ink); }
  .back__stripe .brand__name { font-size: 26px; letter-spacing: 2px; }
</style>
</head>
<body>
<main class="sheet">

  <section class="card card--front" aria-label="Card front">
    <svg class="card__bands" viewBox="0 0 520 298" preserveAspectRatio="none" aria-hidden="true">
      <polygon class="band-blue" points="0,0 520,0 520,96 360,96 340,74 340,20 0,20"/>
      <polygon class="band-green" points="0,210 120,210 140,232 140,278 520,278 520,298 0,298"/>
    </svg>
    <div class="front__brand">
      <span class="brand__dot"></span>
      <span class="brand__name">Brackwell Consulting</span>
    </div>
    <div class="front__details">
      <h1 class="person__name">Euan Brackwell</h1>
      <p class="person__role">Owner</p>
      <ul class="contact">
        <li class="contact__item">
          <svg class="contact__icon" viewBox="0 0 12 12" aria-hidden="true"><rect x="3" y="0.5" width="6" height="11" rx="1.2" fill="none" stroke="#444"/><rect x="4" y="2" width="4" height="6" fill="#444"/></svg>
          07402 916 254
        </li>
        <li class="contact__item">
          <svg class="contact__icon" viewBox="0 0 12 12" aria-hidden="true"><rect x="0.5" y="2" width="11" height="8" fill="#444"/><path d="M0.5 2 L6 7 L11.5 2" fill="none" stroke="#fff"/></svg>
          euan.brackwell@brackwellconsulting.example
        </li>
        <li class="contact__item">
          <svg class="contact__icon" viewBox="0 0 12 12" aria-hidden="true"><circle cx="6" cy="6" r="5.3" fill="none" stroke="#555"/><ellipse cx="6" cy="6" rx="2.3" ry="5.3" fill="none" stroke="#555"/><line x1="0.7" y1="6" x2="11.3" y2="6" stroke="#555"/></svg>
          http://www.brackwellconsulting.example
        </li>
      </ul>
    </div>
  </section>

  <section class="card card--back" aria-label="Card back">
    <svg class="card__bands" viewBox="0 0 520 298" preserveAspectRatio="none" aria-hidden="true">
      <rect class="band-blue" x="0" y="0" width="520" height="112"/>
      <rect class="band-green" x="0" y="186" width="520" height="112"/>
    </svg>
    <div class="back__stripe">
      <span class="brand__dot"></span>
      <span class="back__divider"></span>
      <span class="brand__name">Brackwell Consulting</span>
    </div>
  </section>

</main>
</body>
</html>
```